Halvard Atelier Business cards

Design our business cards and eventually a logo. The company is based in Paris, its activity is the retailing via internet of luxury home furniture (like Vambrelli, Bercusa, tarvoni...) Our clients are international andwith a high sense of aesthetics. The design shall communicate wealth and trust with a high quality and aesthetic sense, pure lines Company Name is Halvard AtelierExplanation of the name: usually people who wants to buy furniture usually go in a showroom. Today they go in showroom to test the furniture and they search for the price on internet, which is a "Halvard atelier".We will not be a e-commerce site. Our site will be (another project) a presentation site which purpose is to reach qualified prospects. Then everything will be handled by phone, meeting etc.The business card must be professional as we will negotiate with many luxury brands, opportunity to represent them on our site, prices etc.As far as the color are concerned mostly black and whithe or grey. The font of the Halvard Atelier name shall have some impact.

Target Market(s)

High-end furniture and buyers of luxury goods, international customers, mostly women who handle such projects.
We also deal with professional buyers (hotels as an example) and luxury brands

Contact Information for Business Card

standard format 85x55, lanscape card, square corners will be printed on thick high quality paper (300 or 350g)

Font styles to use
Sans Serif

Colors

Designer to choose colors to be used in the design.

Requirements
Must have
• Must be white, as the paper will be high quality, the paper will enhance the card.
• Name of the brand Halvard atelier (with specific font which make it very nice looking and catch the attention. similar to Calibri or Calibri
• Name of person (will give you the name later (4 names and position)
• the position of the person
• Mobile phone, e-mail, Physical address 27, rue Fenouillard, 75005 Paris, France (courrier only) our web site www.halvardatelier.fr
• The card must be simple and class
Nice to have
• Font of the address is smaller than the rest,
• Calibri font or similar on recto side with the name of the company which may look similar to the picture inserted in the brief.
• The grey color in the picture inserted is ok for us
Should not have
• Any parallel lines which represent the name of the company
• Any heavy design If you go on internet sites which present the furniture all designs are pure lines and high quality craftsmanship. To have an idea of our targetted client or brand we will be in touch: https://www.casavelumi.it/projects/
• Note that the picture added below is what we use, now as mail signature, up to you to have a better design etc.

```html
<!DOCTYPE html>
<html lang="en">
<head>
<meta charset="utf-8">
<title>Halvard Atelier — Business Card</title>
<link rel="stylesheet" href="https://fonts.googleapis.com/css2?family=Montserrat:wght@500;600;700;800&display=swap">
<style>
  :root {
    --backdrop: #ecedef;
    --card: #ffffff;
    --brand-red: #8c1520;
    --text-grey: #8f8f91;
    --rule-grey: #9c9c9e;
    --band-grey: #a9a9ab;
  }
  * { margin: 0; padding: 0; box-sizing: border-box; }
  html, body {
    width: 1200px;
    height: 900px;
    overflow: hidden;
    background: var(--backdrop);
    font-family: "Montserrat", Arial, sans-serif;
  }
  .card {
    position: absolute;
    left: 100px;
    top: 127px;
    width: 1000px;
    height: 646px;
    background: var(--card);
    box-shadow: 0 10px 30px rgba(0,0,0,0.08);
    overflow: hidden;
  }
  .holder-name {
    position: absolute;
    left: 60px;
    top: 92px;
    font-size: 46px;
    font-weight: 800;
    letter-spacing: 0.5px;
    color: var(--brand-red);
    text-transform: uppercase;
  }
  .divider {
    position: absolute;
    left: 60px;
    top: 156px;
    width: 880px;
    height: 3px;
    background: var(--rule-grey);
  }
  .holder-role {
    position: absolute;
    left: 60px;
    top: 172px;
    font-size: 27px;
    font-weight: 600;
    color: var(--text-grey);
  }
  .contact-list {
    position: absolute;
    left: 60px;
    top: 236px;
    list-style: none;
  }
  .contact-item {
    display: flex;
    align-items: center;
    gap: 18px;
    height: 46px;
    font-size: 26px;
    font-weight: 600;
    color: var(--text-grey);
  }
  .contact-icon { width: 26px; height: 26px; flex: none; }
  .brand-mark {
    position: absolute;
    right: 60px;
    top: 40px;
    text-align: center;
    color: var(--brand-red);
    font-weight: 800;
    line-height: 1;
  }
  .brand-mark .brand-main {
    display: block;
    font-size: 62px;
    letter-spacing: 1px;
  }
  .brand-mark .brand-sub {
    display: block;
    margin-top: 8px;
    font-size: 20px;
    letter-spacing: 14px;
    padding-left: 14px;
  }
  .address {
    position: absolute;
    right: 60px;
    top: 440px;
    text-align: right;
    font-size: 30px;
    font-weight: 600;
    line-height: 1.3;
    color: var(--text-grey);
  }
  .bands {
    position: absolute;
    left: 0;
    bottom: 0;
    width: 1000px;
    height: 96px;
  }
</style>
</head>
<body>
  <main class="card">
    <div class="brand-mark">
      <span class="brand-main">HALVARD</span>
      <span class="brand-sub">ATELIER</span>
    </div>

    <h1 class="holder-name">Mathis Kervoran</h1>
    <div class="divider"></div>
    <p class="holder-role">President and Co-Founder</p>

    <ul class="contact-list">
      <li class="contact-item">
        <svg class="contact-icon" viewBox="0 0 24 24" aria-hidden="true">
          <path fill="var(--brand-red)" d="M6.6 2.5c.6-.4 1.4-.3 1.8.3l2.2 3.3c.4.6.3 1.4-.2 1.8L9 9c.9 2.2 3.2 4.7 5.6 5.8l1.2-1.4c.5-.5 1.2-.6 1.8-.2l3.2 2.1c.6.4.8 1.2.4 1.8l-1.3 2.2c-.7 1.2-2.2 1.8-3.6 1.3C9.7 18.6 5.3 14.2 3.4 7.8 3 6.4 3.5 4.9 4.6 4.1z"/>
        </svg>
        <span>+33641729083</span>
      </li>
      <li class="contact-item">
        <svg class="contact-icon" viewBox="0 0 24 24" aria-hidden="true">
          <circle cx="12" cy="12" r="10" fill="var(--brand-red)"/>
          <g fill="none" stroke="#ffffff" stroke-width="1.4">
            <ellipse cx="12" cy="12" rx="4.2" ry="10"/>
            <line x1="2" y1="12" x2="22" y2="12"/>
            <path d="M4 6.5h16M4 17.5h16"/>
          </g>
        </svg>
        <span>www.halvardatelier.fr</span>
      </li>
    </ul>

    <address class="address" style="font-style: normal;">
      27, rue Fenouillard<br>
      75005 Paris, France
    </address>

    <svg class="bands" viewBox="0 0 1000 96" aria-hidden="true">
      <polygon points="0,30 560,30 600,66 0,66" fill="var(--brand-red)"/>
      <polygon points="588,66 1000,66 1000,92 616,92" fill="var(--band-grey)"/>
    </svg>
  </main>
</body>
</html>
```